Web Page for marketing online agency

We are an online marketing agency that is acing the direct response model. We engage with our customers throughout different marketing techniques as research copy-writing, advertisements and content writing. We would need a website design that will have four main aspects: The Vision; stating who we are, The Mission; stating what we do, The Team And It's Values, and a Contact Form. For this design we would want a sharp, clean and smart approach, with illustrated elements or suggestive images. You can use the attached copy, the logo, the USP and the motto. Please integrate them as you see fit while keeping in mind the previous needs and copy. This website is going to be our connection with our possible partners, future colleagues and even our clients. You may submit a design for one page or integrate the 4 different aspects on separate web pages.
Target Market(s)
business partners, future employees, age range 25-60
Industry/Entity Type
Direct Marketing
Number of Pages Required
1 page
Requirements
Must have
- Menu / Header
- 4 Parts or 4 Pages including: vision, mission, team, contact
- Logo
- Motto: Bright Reach
- USP: We help people help themselves.
- The copy attached
Nice to have
- Representative illustrated images or elements
Should not have
- A boring design, classical design - WordPress like

```html
<!DOCTYPE html>
<html lang="en">
<head>
<meta charset="utf-8">
<title>NovaKin – Bright Reach</title>
<link rel="stylesheet" href="https://fonts.googleapis.com/css2?family=Heebo:wght@300;400;500;700&display=swap">
<style>
  :root {
    --night: #070d1c;
    --deep-navy: #0d1a33;
    --glow-blue: #3a74b8;
    --white: #ffffff;
    --frame-grey: #5d6068;
    --brand-ink: #1b1d24;
    --heading-navy: #24305e;
    --label-slate: #8a93b8;
    --body-grey: #6d7186;
    --accent-cyan: #2aa7df;
  }
  * { box-sizing: border-box; margin: 0; padding: 0; }
  html, body { width: 1200px; height: 676px; overflow: hidden; background: var(--white); }
  body { font-family: "Heebo", Arial, sans-serif; color: var(--white); }
  a { text-decoration: none; }

  .page { position: relative; width: 1200px; height: 676px; overflow: hidden; }

  /* Hero */
  .hero {
    position: relative; height: 480px;
    background: linear-gradient(180deg, var(--night) 0%, var(--deep-navy) 55%, #13284a 100%);
    overflow: hidden;
  }
  .hero-visual {
    position: absolute; left: 0; top: 150px; width: 1200px; height: 330px;
    background:
      radial-gradient(ellipse 55% 30% at 62% 45%, rgba(120,170,230,.55), rgba(58,116,184,.18) 60%, transparent 80%),
      radial-gradient(ellipse 40% 25% at 85% 25%, rgba(160,200,245,.35), transparent 75%),
      radial-gradient(ellipse 50% 30% at 35% 80%, rgba(58,116,184,.3), transparent 80%);
  }

  .brand {
    position: absolute; left: 30px; top: 0; width: 200px; height: 110px;
    background: var(--white); border: 6px solid var(--frame-grey); border-top: 0;
    display: flex; align-items: center; justify-content: center; gap: 8px;
  }
  .brand-name { font-weight: 500; font-size: 27px; color: var(--brand-ink); letter-spacing: .5px; }
  .brand-dot { width: 14px; height: 14px; border-radius: 50%; background: var(--accent-cyan); }

  .main-nav { position: absolute; left: 370px; top: 34px; display: flex; gap: 34px; }
  .main-nav a { color: var(--white); font-size: 13px; font-weight: 500; letter-spacing: .2px; }

  .header-actions { position: absolute; right: 50px; top: 26px; display: flex; gap: 8px; }
  .btn-outline, .btn-solid {
    font-size: 12px; border-radius: 16px; padding: 6px 11px; line-height: 1;
    border: 1.5px solid var(--white);
  }
  .btn-outline { color: var(--white); }
  .btn-solid { background: var(--white); color: var(--brand-ink); font-weight: 500; }

  .hero-copy { position: absolute; left: 40px; top: 210px; }
  .usp { font-weight: 300; font-size: 27px; letter-spacing: -.2px; }
  .motto { font-weight: 300; font-size: 20px; margin-top: 6px; margin-left: 4px; }
  .btn-learn {
    display: inline-block; margin-top: 22px; margin-left: 6px;
    border: 1.5px solid var(--white); border-radius: 16px;
    padding: 5px 22px; font-size: 12px; color: var(--white); font-weight: 300;
  }

  /* Vision */
  .vision { position: relative; height: 196px; padding: 30px 0 0 60px; color: var(--heading-navy); }
  .section-label { font-size: 15px; font-weight: 300; color: var(--label-slate); line-height: 18px; }
  .section-title { font-size: 29px; font-weight: 400; line-height: 36px; margin-top: 2px; }
  .vision-intro { font-size: 13px; font-weight: 300; color: var(--body-grey); width: 470px; line-height: 19px; margin-top: 12px; }
  .vision-points { list-style: none; margin-top: 10px; }
  .vision-points li {
    display: flex; align-items: center; gap: 10px;
    font-size: 13px; font-weight: 300; color: var(--body-grey); line-height: 18px; margin-bottom: 8px;
  }
  .tick { width: 12px; height: 12px; flex: none; }
  .vision-illustration {
    position: absolute; left: 900px; top: 84px; width: 66px; height: 120px;
    background: linear-gradient(180deg, #1f9ad6 0%, #33b4e8 45%, #5ccaf0 100%);
    border-radius: 33px 33px 4px 4px;
  }
</style>
</head>
<body>
<div class="page">
  <header class="hero">
    <div class="hero-visual" role="img" aria-label="Glowing blue network of connected points spreading across a dark sky"></div>

    <a class="brand" href="#">
      <span class="brand-name">NovaKin</span>
      <span class="brand-dot"></span>
    </a>

    <nav class="main-nav">
      <a href="#vision">OUR VISION</a>
      <a href="#mission">OUR MISSION</a>
      <a href="#team">TEAM</a>
      <a href="#contact">CONTACT</a>
    </nav>

    <div class="header-actions">
      <a class="btn-outline" href="#">Log In</a>
      <a class="btn-solid" href="#contact">Wanna Talk?</a>
    </div>

    <div class="hero-copy">
      <h1 class="usp">We help people help themselves</h1>
      <p class="motto">NovaKin - Bright Reach</p>
      <a class="btn-learn" href="#vision">Learn More</a>
    </div>
  </header>

  <section class="vision" id="vision">
    <p class="section-label">The Vision</p>
    <h2 class="section-title">Who we are ?</h2>
    <p class="vision-intro">We are a direct response company that creates and sells information products and services that millions of people find interesting and important in their lives</p>
    <ul class="vision-points">
      <li><svg class="tick" viewBox="0 0 12 12"><path d="M1.5 6.5 L4.5 9.5 L10.5 2.5" fill="none" stroke="#2aa7df" stroke-width="2"/></svg>We are specialized in the self-reliance market and we serve conservative Americans.</li>
      <li><svg class="tick" viewBox="0 0 12 12"><path d="M1.5 6.5 L4.5 9.5 L10.5 2.5" fill="none" stroke="#2aa7df" stroke-width="2"/></svg>We are in this business to serve globally and to grow individually</li>
    </ul>
    <div class="vision-illustration" role="img" aria-label="Illustration of a light bulb rising above a blue tower"></div>
  </section>
</div>
</body>
</html>
```